Web design for construction/ handyman company. We are a new company and trying to brand ourselves.

We have a logo with a character already in place and want a user friendly and simple site. I'm attaching our logo designs with our Crocodile character to get an idea of our logo. We want people to remember us and our site. The name we chose was so we could use a logo with a character. Our name is Pelican Builders LLC.

Target Market(s)

New clients

Industry/Entity Type

Contractor

Coding

Coded - Design and coding required

Number of Pages Required

4 page

Font styles to use
Sans Serif

Requirements
Must have
• About Us Page, What we do (not sure what to call this), Contact Us, Home Page. Would like the same colors as on our business card designs to be used on the website.
Nice to have
• We eventually want a project page to add photos of projects but thats not necessary now. Would be nice to use the crocodile theme, hammer or something similar somehow in the page names or clicks.

```html
<!DOCTYPE html>
<html lang="en">
<head>
<meta charset="utf-8">
<title>Pelican Builders LLC</title>
<link rel="stylesheet" href="https://fonts.googleapis.com/css2?family=Open+Sans:wght@400;600;700;800&display=swap">
<style>
:root{
  --blue:#1a67ad;
  --blue-dark:#0f4f8c;
  --blue-deep:#0b3f73;
  --green:#5db52c;
  --green-light:#a6dc6f;
  --green-pale:#e6f5d4;
  --ink:#333;
  --muted:#777;
  --grey-band:#ececec;
  --white:#fff;
}
*{box-sizing:border-box;margin:0;padding:0}
html,body{width:1200px;height:2312px;overflow:hidden}
body{position:relative;font-family:"Open Sans",Arial,sans-serif;color:var(--ink);background:var(--white)}
.abs{position:absolute}

/* header */
.site-header{left:0;top:0;width:1200px;height:120px;background:var(--white)}
.brand{left:60px;top:34px;display:flex;align-items:center;gap:12px}
.brand-dot{width:44px;height:44px;border-radius:50%;background:var(--green)}
.brand-name{font-size:24px;font-weight:800;color:var(--blue)}
.call-us{right:60px;top:18px;font-size:13px;font-weight:700;color:var(--ink)}
.call-us span{color:var(--blue)}
.main-nav{right:60px;top:60px;display:flex;gap:30px;align-items:center;font-size:13px;font-weight:700;color:var(--ink)}
.main-nav .active{color:var(--blue);border-bottom:3px solid var(--green);padding-bottom:6px}

/* hero */
.hero{left:0;top:120px;width:1200px;height:480px;background:linear-gradient(180deg,#d9d4cb 0%,#b9ad9c 45%,#8d7d69 100%)}
.hero-title{left:0;top:230px;width:1200px;text-align:center;color:var(--white);font-size:58px;font-weight:800;letter-spacing:1px}
.hero-sub{left:0;top:310px;width:1200px;text-align:center;color:var(--white);font-size:24px;font-weight:700;letter-spacing:1px}
.hero-arrow{top:265px}

/* welcome */
.welcome{left:0;top:540px;width:1200px;height:400px}
.welcome-title{left:0;top:205px;width:1200px;text-align:center;color:var(--white);font-size:22px;font-weight:700}
.welcome-text{left:250px;top:250px;width:700px;text-align:center;color:var(--white);font-size:12px;line-height:19px}
.btn-outline{left:540px;top:335px;width:120px;height:34px;border:2px solid var(--white);color:var(--white);font-size:12px;font-weight:700;display:flex;align-items:center;justify-content:center;background:rgba(255,255,255,.15)}

/* projects */
.section-title{font-size:22px;font-weight:700;color:var(--ink);text-align:center}
.projects-title{left:0;top:1005px;width:1200px}
.project-card{top:1070px;width:232px}
.project-photo{width:232px;height:132px;border:4px solid var(--white);box-shadow:0 0 0 1px #ddd}
.project-name{margin-top:22px;font-size:13px;font-weight:700}
.project-text{margin-top:10px;font-size:12px;line-height:19px;color:var(--muted)}
.read-link{margin-top:12px;font-size:12px;font-weight:700;color:var(--blue)}

/* pricing band */
.pricing-band{left:0;top:1420px;width:1200px;height:200px;background:linear-gradient(180deg,#f6f6f6,var(--grey-band))}
.pricing-text{left:260px;top:1450px;width:680px;text-align:center;font-size:14px;line-height:22px;color:#555}
.btn-blue{left:530px;top:1525px;width:140px;height:36px;background:var(--blue);color:var(--white);font-size:12px;font-weight:700;display:flex;align-items:center;justify-content:center;border-radius:2px}

/* about / services */
.col-title{font-size:22px;font-weight:700;color:var(--ink)}
.col-rule{height:2px;background:var(--green);width:60px;margin-top:8px}
.about-photo{left:100px;top:1720px;width:220px;height:200px;background:linear-gradient(135deg,#c9b9a0,#8a7a65)}
.about-text{left:340px;top:1718px;width:240px;font-size:12px;line-height:19px;color:var(--muted)}
.btn-small{width:110px;height:32px;background:var(--blue);color:var(--white);font-size:12px;font-weight:700;display:flex;align-items:center;justify-content:center;border-radius:2px}
.service{left:620px;width:480px;display:flex;gap:20px}
.service-photo{width:100px;height:80px;flex:none;background:linear-gradient(135deg,#a9c3d8,#6f8ea5)}
.service-name{font-size:13px;font-weight:700;color:var(--ink)}
.service-text{margin-top:8px;font-size:12px;line-height:19px;color:var(--muted)}

/* footer */
.footer{left:0;top:2020px;width:1200px;height:292px}
.foot-col{top:2090px;color:var(--white)}
.foot-title{font-size:13px;font-weight:700;margin-bottom:16px}
.foot-links{list-style:none;font-size:12px;line-height:22px}
.foot-text{font-size:12px;line-height:19px;width:200px}
.foot-input{margin-top:10px;width:200px;height:28px;background:var(--white);color:#999;font-size:11px;padding:6px 8px}
.btn-green{margin-top:10px;width:80px;height:28px;background:var(--green);color:var(--white);font-size:12px;font-weight:700;display:flex;align-items:center;justify-content:center}
.social-row,.contact-row{display:flex;align-items:center;gap:10px;font-size:12px;margin-bottom:12px}
.social-box{width:22px;height:22px;background:var(--white);border-radius:3px;flex:none}
.copyright{left:0;top:2272px;width:1200px;height:40px;background:var(--blue-deep);color:#cfe0f0;font-size:11px;display:flex;align-items:center;justify-content:center}
</style>
</head>
<body>

<header class="site-header abs">
  <div class="brand abs"><span class="brand-dot"></span><span class="brand-name">Pelican Builders LLC</span></div>
  <div class="call-us abs">CALL US NOW : <span>(555) 014-2290</span></div>
  <nav class="main-nav abs">
    <span class="active">HOME</span><span>ABOUT US</span><span>WHAT WE DO</span><span>PRICING</span><span>CONTACT US</span>
    <svg width="14" height="14" viewBox="0 0 14 14"><circle cx="6" cy="6" r="4.5" fill="none" stroke="#1a67ad" stroke-width="2"/><line x1="9.5" y1="9.5" x2="13" y2="13" stroke="#1a67ad" stroke-width="2"/></svg>
  </nav>
</header>

<section class="hero abs" role="img" aria-label="Photo of a finished kitchen with island and bar stools"></section>
<svg class="hero-arrow abs" style="left:20px" width="24" height="40" viewBox="0 0 24 40"><polyline points="18,4 4,20 18,36" fill="none" stroke="#fff" stroke-width="4"/></svg>
<svg class="hero-arrow abs" style="right:20px" width="24" height="40" viewBox="0 0 24 40"><polyline points="6,4 20,20 6,36" fill="none" stroke="#fff" stroke-width="4"/></svg>
<h1 class="hero-title abs">PELICANBUILDERS</h1>
<p class="hero-sub abs">WE ARE A CONSTRUCTION &amp; HANDYMAN COMPANY</p>

<section class="welcome abs">
  <svg class="abs" style="left:0;top:0" width="1200" height="400" viewBox="0 0 1200 400">
    <defs>
      <linearGradient id="welcomeFill" x1="0" y1="0" x2="0" y2="1">
        <stop offset="0" stop-color="#a6dc6f"/>
        <stop offset=".45" stop-color="#5db52c"/>
        <stop offset=".85" stop-color="#9ed566"/>
        <stop offset="1" stop-color="#e6f5d4"/>
      </linearGradient>
    </defs>
    <path d="M0 60 Q600 -20 1200 60 L1200 400 L0 400 Z" fill="url(#welcomeFill)"/>
    <path d="M0 60 Q600 -20 1200 60" fill="none" stroke="#fff" stroke-width="4"/>
  </svg>
  <h2 class="welcome-title abs">WELCOME TO PELICANBUILDERS</h2>
  <p class="welcome-text abs">Since day one we have built homes, kitchens and decks with honest prices and careful hands. Our crew handles new construction, repairs and remodels across the county, and every job gets the same attention to detail. Tell us about your project and we will plan it with you, step by step, from first sketch to final clean up.</p>
  <div class="btn-outline abs">READ MORE</div>
</section>

<h2 class="section-title projects-title abs">LATEST PROJECTS</h2>

<article class="project-card abs" style="left:100px">
  <div class="project-photo" role="img" aria-label="Project photo of a remodeled kitchen" style="background:linear-gradient(135deg,#d6cbb8,#9a8870)"></div>
  <h3 class="project-name">FINIBUS BONORUM ETMAL</h3>
  <p class="project-text">Full kitchen remodel with new cabinets, stone counters and lighting, finished on time.</p>
  <p class="read-link">READ MORE</p>
</article>
<article class="project-card abs" style="left:356px">
  <div class="project-photo" role="img" aria-label="Project photo of a backyard deck and garden" style="background:linear-gradient(135deg,#9fbf7a,#5e7f3e)"></div>
  <h3 class="project-name">FINIBUS BONORUM ETMAL</h3>
  <p class="project-text">Backyard deck and fence built from treated timber for a family home.</p>
  <p class="read-link">READ MORE</p>
</article>
<article class="project-card abs" style="left:612px">
  <div class="project-photo" role="img" aria-label="Project photo of a renovated living room" style="background:linear-gradient(135deg,#d9c7ad,#a07e5a)"></div>
  <h3 class="project-name">FINIBUS BONORUM ETMAL</h3>
  <p class="project-text">Living room refresh with new flooring, trim work and fresh paint.</p>
  <p class="read-link">READ MORE</p>
</article>
<article class="project-card abs" style="left:868px">
  <div class="project-photo" role="img" aria-label="Project photo of an open plan kitchen and dining area" style="background:linear-gradient(135deg,#e3dccf,#a99a85)"></div>
  <h3 class="project-name">FINIBUS BONORUM ETMAL</h3>
  <p class="project-text">Open plan kitchen and dining area with custom island and shelving.</p>
  <p class="read-link">READ MORE</p>
</article>

<section class="pricing-band abs"></section>
<p class="pricing-text abs">Sed ut perspiciatis unde omnis iste natus error sit voluptatem accusantium doloremque laudantium, totam rem aperiam, eaque ipsa quae ab illo inventore veritatis et quasi architecto beatae.</p>
<div class="btn-blue abs">OUR PRICING</div>

<section class="abs" style="left:100px;top:1655px">
  <h2 class="col-title">ABOUT US</h2>
  <div class="col-rule"></div>
</section>
<div class="about-photo abs" role="img" aria-label="Photo of a smiling builder with tools"></div>
<div class="about-text abs">
  <p>We are a local team of builders and handymen who care about doing the job right. From small fixes to full renovations, we show up on time, keep the site clean and explain every step. Our goal is simple: work you are proud of and a crew you will call again.</p>
</div>
<div class="btn-small abs" style="left:340px;top:1940px">READ MORE</div>

<section class="abs" style="left:620px;top:1655px">
  <h2 class="col-title">WHAT WE DO</h2>
  <div class="col-rule"></div>
</section>
<article class="service abs" style="top:1720px">
  <div class="service-photo" role="img" aria-label="Photo of a construction site"></div>
  <div>
    <h3 class="service-name">CONSTRUCTION</h3>
    <p class="service-text">New homes, additions and garages built to code, managed by one crew from start to finish.</p>
  </div>
</article>
<article class="service abs" style="top:1840px">
  <div class="service-photo" role="img" aria-label="Photo of handyman tools on a workbench" style="background:linear-gradient(135deg,#c8b79c,#8d7355)"></div>
  <div>
    <h3 class="service-name">HANDYMAN WORK</h3>
    <p class="service-text">Repairs, installs and small jobs around the house, done quickly and priced fairly.</p>
  </div>
</article>

<footer class="footer abs">
  <svg class="abs" style="left:0;top:0" width="1200" height="292" viewBox="0 0 1200 292">
    <defs>
      <linearGradient id="footFill" x1="0" y1="0" x2="0" y2="1">
        <stop offset="0" stop-color="#2a7bc2"/>
        <stop offset="1" stop-color="#0f4f8c"/>
      </linearGradient>
    </defs>
    <path d="M0 50 Q300 0 600 30 T1200 20 L1200 292 L0 292 Z" fill="url(#footFill)"/>
  </svg>
</footer>

<div class="foot-col abs" style="left:100px">
  <h4 class="foot-title">QUICK LINKS</h4>
  <ul class="foot-links"><li>Home</li><li>About us</li><li>What we do</li><li>Pricing</li><li>Contact us</li></ul>
</div>
<div class="foot-col abs" style="left:330px">
  <h4 class="foot-title">NEWSLETTER</h4>
  <p class="foot-text">Register your email below to get news and offers.</p>
  <div class="foot-input">Email Address</div>
  <div class="btn-green">SIGN UP</div>
</div>
<div class="foot-col abs" style="left:640px">
  <h4 class="foot-title">FOLLOW US ON</h4>
  <div class="social-row"><span class="social-box"></span>Social page</div>
  <div class="social-row"><span class="social-box"></span>News feed</div>
  <div class="social-row"><span class="social-box"></span>Photo feed</div>
</div>
<div class="foot-col abs" style="left:860px;width:260px">
  <h4 class="foot-title">NEWSLETTER</h4>
  <div class="contact-row">
    <svg width="14" height="18" viewBox="0 0 14 18"><path d="M7 1C3.7 1 1 3.6 1 6.9 1 11 7 17 7 17s6-6 6-10.1C13 3.6 10.3 1 7 1z" fill="#fff"/><circle cx="7" cy="7" r="2.2" fill="#1a67ad"/></svg>
    <span>Pelican Builders LLC, 418 Harbor Road, Austin, TX 78701</span>
  </div>
  <div class="contact-row">
    <svg width="14" height="14" viewBox="0 0 14 14"><path d="M3 1l2.5 3-1.5 1.5c.8 1.8 2.2 3.2 4 4L9.5 8l3 2.5-1.5 2.5C6 13 1 8 1 2.5z" fill="#fff"/></svg>
    <span>(555) 014-2290</span>
  </div>
  <div class="contact-row">
    <svg width="14" height="12" viewBox="0 0 14 12"><rect x="1" y="1" width="12" height="10" fill="none" stroke="#fff" stroke-width="1.5"/><polyline points="1,1 7,7 13,1" fill="none" stroke="#fff" stroke-width="1.5"/></svg>
    <span>hello@pelicanbuilders.example</span>
  </div>
</div>

<div class="copyright abs">Copyright © Pelican Builders LLC. All Rights Reserved.</div>

</body>
</html>
```